We need a poster the the 47th Annual Larkmoor Quarter FestaWalk to be held May 21-22, 2016. It's the longest running festival of its kind in the United States. In 1970, community leaders established the FestaWalk to heal our community after protests, street riots, and violence disrupted the community. Originally a blanket-vending event with lots of free live music, the Larkmoor Quarter FestaWalk has become a regional event that features handmade products by individual artists and craftsmen. In celebration of the international flavor of our community, we invite food vendors to participate along with our many local restaurants to present an around-the-world culinary experience.
Seattle’s first modern street fair was held on May 23-24, 1970. Police closed Fennick Row NE to traffic from NE 62nd Street to 38th Street and turned over “The Row” to 300 vendors and artists who catered to over 50,000 visitors during the weekend. The Larkmoor Quarter FestaWalk was the brainchild of Kenji Torrell (1919-1993), a Japanese American merchant in the L Quarter and longtime pacifist, assisted by Bravant executive Walt Gribsby.
The success of the first Larkmoor Quarter FestaWalk was all the more remarkable given the social and political tensions of the time. Riots had divided the L Quarter community on several nights in August of 1969 and only weeks earlier thousands of NPC students had protested the United States invasion of Cambodia and the killings of four demonstrating students at Oberford Tech.
The proposal to close Fennick Row NE was greeted with much skepticism by area businesses, but the fair proved to be a tremendous success. The Larkmoor Quarter FestaWalk has inspired other Seattle neighborhoods to stage similar events in their business districts. The event is currently presented by The L Quarter Alliance a 501(c)(3) nonprofit.
For more information, please checkout our website www.lquarterfestawalk-demo.org or contact Marian Thistlewood, President & CEO of The L Quarter Alliance at marian.thistlewood@lquarteralliance-demo.org. Thank you!

Target Market(s)

Residents of the Puget Sound Region of the State of Washington

Industry/Entity Type

Festival

Font styles to use
Serif

Requirements
Must have
• It will be used for signs on city buses and souvenir t-shirts
Nice to have
• Bright colors

```html
<!DOCTYPE html>
<html lang="en">
<head>
<meta charset="utf-8">
<title>47th Annual Larkmoor Quarter FestaWalk</title>
<link rel="stylesheet" href="https://fonts.googleapis.com/css2?family=Arimo:wght@700&family=Libre+Bodoni:wght@700&display=swap">
<style>
  :root {
    --aqua: #98ecea;
    --sky: #5aa2f8;
    --navy: #150d46;
    --indigo: #262a7e;
    --blue: #3b6cc4;
    --orange: #ff4200;
    --title-blue: #0c0c92;
    --title-shadow: #5f6fb8;
    --white: #ffffff;
  }
  html, body {
    margin: 0;
    padding: 0;
    width: 849px;
    height: 1200px;
    overflow: hidden;
    background: var(--navy);
  }
  .poster {
    display: block;
    width: 849px;
    height: 1200px;
  }
  .title {
    font-family: "Libre Bodoni", "Bodoni Moda", Georgia, serif;
    font-weight: 700;
    fill: var(--title-blue);
    filter: drop-shadow(2px 2px 0 var(--title-shadow));
  }
  .word {
    font-family: "Arimo", Arial, Helvetica, sans-serif;
    font-weight: 700;
    fill: var(--white);
  }
  .date-line { letter-spacing: 2px; }
</style>
</head>
<body>
<svg class="poster" viewBox="0 0 1061 1500" xmlns="http://www.w3.org/2000/svg" role="img" aria-label="Poster for the 47th Annual Larkmoor Quarter FestaWalk, 21 and 22 May 2016, Seattle">
  <defs>
    <linearGradient id="backdropFade" gradientUnits="userSpaceOnUse" x1="0" y1="0" x2="0" y2="1500">
      <stop offset="0" stop-color="#98ecea"/>
      <stop offset="0.24" stop-color="#5aa2f8"/>
      <stop offset="0.32" stop-color="#150d46"/>
      <stop offset="0.55" stop-color="#262a7e"/>
      <stop offset="0.8" stop-color="#3b6cc4"/>
      <stop offset="0.88" stop-color="#ff4200"/>
      <stop offset="1" stop-color="#ff4200"/>
    </linearGradient>
  </defs>

  <rect class="backdrop" x="0" y="0" width="1061" height="1500" fill="url(#backdropFade)" role="img" aria-label="City skyline at dusk with light rays, a street sign and the street below"/>

  <g class="headline">
    <text class="title" x="52" y="280" font-size="236" textLength="228" lengthAdjust="spacingAndGlyphs">47</text>
    <text class="title" x="298" y="160" font-size="98" textLength="420" lengthAdjust="spacingAndGlyphs">th Annual</text>
    <text class="title" x="425" y="270" font-size="100" textLength="425" lengthAdjust="spacingAndGlyphs">Larkmoor</text>
    <text class="title" x="45" y="358" font-size="84" textLength="590" lengthAdjust="spacingAndGlyphs">Quarter FestaWalk</text>
  </g>

  <g class="dates">
    <text class="word" x="465" y="475" font-size="96" textLength="115" lengthAdjust="spacingAndGlyphs">21</text>
    <text class="word" x="455" y="530" font-size="72" textLength="140" lengthAdjust="spacingAndGlyphs">may</text>
    <text class="word date-line" x="602" y="531" font-size="34" textLength="286" lengthAdjust="spacingAndGlyphs">2016 -seattle</text>
    <text class="word" x="465" y="632" font-size="96" textLength="113" lengthAdjust="spacingAndGlyphs">22</text>
  </g>

  <g class="route">
    <text class="word" transform="translate(500,1222) rotate(-90)" font-size="52" textLength="457" lengthAdjust="spacingAndGlyphs">along fennick</text>
    <text class="word" transform="translate(566,890) rotate(-90)" font-size="50" textLength="230" lengthAdjust="spacingAndGlyphs">ROW NE</text>
    <text class="word" transform="translate(566,1190) rotate(-90)" font-size="72" textLength="215" lengthAdjust="spacingAndGlyphs">music</text>
  </g>

  <g class="themes">
    <text class="word" transform="translate(73,1296) rotate(-90)" font-size="46" textLength="750" lengthAdjust="spacing">neighborhood  peace</text>
    <text class="word" x="94" y="890" font-size="46" textLength="161" lengthAdjust="spacingAndGlyphs">metals</text>
    <text class="word" x="88" y="985" font-size="96" textLength="170" lengthAdjust="spacingAndGlyphs">jazz</text>
    <text class="word" transform="translate(358,1016) rotate(-90)" font-size="48" textLength="396" lengthAdjust="spacing">live shows</text>
    <text class="word" x="92" y="1162" font-size="96" textLength="353" lengthAdjust="spacingAndGlyphs">people</text>
    <text class="word" x="298" y="1298" font-size="72" textLength="390" lengthAdjust="spacingAndGlyphs">sculpture</text>
    <text class="word" x="38" y="1437" font-size="142" textLength="527" lengthAdjust="spacingAndGlyphs">culture</text>
    <text class="word" x="582" y="1395" font-size="126" textLength="308" lengthAdjust="spacingAndGlyphs">craft</text>
    <text class="word" transform="translate(686,1210) rotate(-90)" font-size="44" textLength="645" lengthAdjust="spacing">community  celebration</text>
    <text class="word" transform="translate(815,1072) rotate(-90)" font-size="96" textLength="517" lengthAdjust="spacingAndGlyphs">paintings</text>
    <text class="word" transform="translate(882,1258) rotate(-90)" font-size="50" textLength="568" lengthAdjust="spacing">tradition</text>
    <text class="word" transform="translate(1022,1262) rotate(-90)" font-size="106" textLength="1052" lengthAdjust="spacing">food festival</text>
  </g>
</svg>
</body>
</html>
```